Modern design for a Septic Tank maintenance company

Task Description
- The design should be based around the attached HPID (home page information design) called Tane Drain Septic Services HPID. The table boxes are just for approximate placement of information – you DON'T have to make it look exactly like this.
- Information only is in orange text. Copy to go on the design in black text. Some instructions are in the HPID. Please be creative! You don’t have to use the exact images provided if you have a better idea.

- The design needs to be clean and spacious. Please use the colours from the logos in the website design. LOTS of white too. Don't need to use all the images attached some are customer supplied and might only be good for the smaller images.

I've attached home page gallery example photo called Piha beach. You can use this or something similar - be creative please!

Width of content will be 1100 pixels when implemented as a web page. Header height (without nav bar) 150-160 pixels.

The winning PSD file will have to be provided as follows…
1. Canvas size of 2000px x 2000px - 72ppi in Adobe Photoshop (CS5 compatible)
2. Width of content section is 1100px wide - centered in the canvas
3. Any button rollovers/hovers in the PSD as hidden layers.
4. All fonts used must be Google fonts (except for the fonts in the header at the top of the page).
5. You will need to supply the chosen home page plus one example page (example page as a style guide for how all other pages will look). Example page is only the header and navigational bar at the top, an empty sector in the middle with a column (180 px wide) which can be left or right aligned which means the main sector is 920 pixels wide, and then the footer at the bottom of the page.

```html
<!DOCTYPE html>
<html lang="en">
<head>
<meta charset="utf-8">
<title>Tane Drain Septic Services</title>
<link rel="stylesheet" href="https://fonts.googleapis.com/css2?family=Ubuntu:wght@400;500;700&family=Raleway:wght@400;500;600&display=swap">
<style>
:root{
  --green:#0fa44f;
  --green-dark:#078a3e;
  --green-deep:#056b30;
  --ink:#2a2a2a;
  --text:#3b3b3b;
  --band:#262626;
  --field:#1b1b1b;
  --field-line:#3a3a3a;
  --footer:#eeeeee;
  --white:#ffffff;
}
*{box-sizing:border-box;margin:0;padding:0}
html,body{width:903px;height:1200px;overflow:hidden}
body{position:relative;background:var(--white);font-family:"Raleway",sans-serif;color:var(--text)}
.abs{position:absolute}
.top-wash{left:0;top:0;width:903px;height:294px;background:linear-gradient(#ffffff,#ededed);border-bottom:1px solid #dcdcdc}

.brand{left:121px;top:20px;display:flex;align-items:center;gap:8px}
.brand-dot{width:22px;height:22px;border-radius:50%;background:var(--green)}
.brand-name{font-family:"Ubuntu",sans-serif;font-weight:500;font-size:17px;color:#1f7c6e}
.tagline{left:303px;top:17px;width:260px;padding-left:16px;border-left:1px solid #cfcfcf;font-size:9px;line-height:16px;color:var(--ink)}
.contact{left:563px;top:17px;width:219px;padding-left:25px;border-left:1px solid #cfcfcf;font-size:9px;line-height:18px;text-align:right;color:var(--ink)}
.contact strong{font-family:"Ubuntu",sans-serif;color:var(--green);font-weight:500}

.nav{left:121px;top:55px;width:661px;height:49px;background:linear-gradient(var(--green),var(--green-dark));display:flex}
.nav a{font-family:"Ubuntu",sans-serif;font-weight:500;font-size:9.5px;color:var(--white);text-decoration:none;display:flex;align-items:center;padding:0 10px;border-right:1px solid rgba(0,0,0,.12)}
.nav a.active{background:var(--green-deep);padding:0 23px}

.hero{left:121px;top:104px;width:661px;height:303px;background:linear-gradient(#7d7a86 0%,#c99a8e 35%,#e8a184 52%,#6f6670 70%,#3f3a3f 100%)}
.hero-box{left:132px;top:158px;width:281px;height:182px;background:rgba(40,40,40,.72);padding:22px 10px 0 10px}
.hero-box h1{font-family:"Ubuntu",sans-serif;font-weight:700;font-size:17px;line-height:22px;color:var(--green);text-transform:uppercase}
.hero-box p{margin-top:8px;font-size:11.5px;line-height:14.5px;color:var(--white)}
.dots{left:136px;top:378px;display:flex;gap:5px}
.dots span{width:8px;height:8px;border-radius:50%;background:var(--white)}
.dots span:first-child{background:var(--green)}

.card{top:413px;width:213px}
.card-head{height:57px;background:var(--green);padding:16px 21px 0;font-family:"Ubuntu",sans-serif;font-weight:700;font-size:11px;line-height:13.5px;color:var(--white);position:relative}
.card-head::after{content:"";position:absolute;left:30px;bottom:-7px;border:7px solid transparent;border-bottom:0;border-top-color:var(--green)}
.card-photo{height:128px}
.card p{margin-top:17px;font-size:8.4px;line-height:16px;color:var(--text)}
.btn{display:inline-flex;align-items:center;justify-content:center;background:var(--green);color:var(--white);font-family:"Ubuntu",sans-serif;font-weight:700;font-size:9px;border-radius:4px}
.card .btn{margin-top:13px;width:72px;height:22px}

.enquiry{left:0;top:784px;width:903px;height:166px;background:var(--band)}
.enq-label{left:146px;top:819px;font-family:"Ubuntu",sans-serif;font-weight:700;font-size:12px;color:var(--white)}
.enq-title{left:145px;top:833px;font-family:"Ubuntu",sans-serif;font-size:20px;color:var(--green)}
.enq-note{left:146px;top:861px;font-size:9px;line-height:13.5px;color:var(--white)}
.field{width:181px;height:25px;background:var(--field);border:1px solid var(--field-line);font-size:7.5px;color:#bdbdbd;padding:8px 6px}
.field.details{width:181px;height:91px;padding:8px 11px}
.send{left:697px;top:910px;width:71px;height:22px}

.footer{left:0;top:950px;width:903px;height:250px;background:var(--footer)}
.foot-head{font-family:"Ubuntu",sans-serif;font-weight:700;font-size:9px;color:var(--green)}
.links{left:121px;top:1000px;list-style:none;font-size:9px;line-height:16px;color:var(--ink)}
.guarantee{left:277px;top:1000px;width:222px;font-size:9px;line-height:16px;color:var(--ink)}
.promo{left:514px;width:268px;height:63px;border-radius:4px;background:linear-gradient(#18c062,#07883c);display:flex;align-items:center;padding-left:12px;gap:13px;color:var(--white);font-size:9px;line-height:16px;box-shadow:0 2px 2px rgba(0,0,0,.2)}
.promo strong{font-family:"Ubuntu",sans-serif;font-weight:700}
.copy{left:121px;top:1168px;font-size:9px;color:var(--ink)}
.social{left:711px;top:1164px;display:flex;gap:5px}
.social span{width:20px;height:20px;border-radius:50%}
</style>
</head>
<body>
<div class="abs top-wash"></div>

<div class="abs brand"><span class="brand-dot"></span><span class="brand-name">Tane Drain</span></div>
<p class="abs tagline">Our Septic tank maintenance services will help your septic system perform at optimum efficiency</p>
<p class="abs contact">For Septic Tank servicing, installation and parts<br><strong>Auckland Wide &nbsp;09 555 0142 | 021 555 01 888</strong></p>

<nav class="abs nav">
  <a class="active">Home</a><a>About</a><a>Deciphering Your Septic tank</a><a>Servicing &amp; Maintenance</a><a>Parts</a><a>Free Quote</a><a>Contact</a>
</nav>

<div class="abs hero" role="img" aria-label="Sunset beach scene with a surfer walking along the shore"></div>
<div class="abs hero-box">
  <h1>Want to learn more about how your septic tank works ?</h1>
  <p>Tane Drain Septic Services are Auckland’s best septic tank experts and will tell you everything there is to know...</p>
</div>
<div class="abs dots"><span></span><span></span><span></span><span></span></div>

<div class="abs card" style="left:121px">
  <div class="card-head">Looking for septic tanks parts in Auckland asap?</div>
  <div class="card-photo" role="img" aria-label="Septic pumps and replacement parts" style="background:linear-gradient(#7d8a7a,#a9a29a)"></div>
  <p>If you need replacement parts for septic tanks, call us today! Tane Drain Septic Services will either have or can source the part you need fast and offer septic tank part installation services to ensure your parts are fitted orrectly and work at optimum efficiency for longer. And often we can offer same day service when you’re in a bind.</p>
  <span class="btn">More Info</span>
</div>
<div class="abs card" style="left:345px">
  <div class="card-head">Want to know how to take care of your septic tank?</div>
  <div class="card-photo" role="img" aria-label="Garden area above a septic tank" style="background:linear-gradient(#4b6048,#8b8a76)"></div>
  <p>If you need replacement parts for septic tanks, call us today! Tane Drain Septic Services will either have or can source the part you need fast and offer septic tank part installation services to ensure your parts are fitted orrectly and work at optimum efficiency for longer. And often we can offer same day service when you’re in a bind.</p>
  <span class="btn">More Info</span>
</div>
<div class="abs card" style="left:569px">
  <div class="card-head">When was the last time you serviced your septic tank?</div>
  <div class="card-photo" role="img" aria-label="Septic tank lids on a lawn" style="background:linear-gradient(#6a6f58,#6d9a3a)"></div>
  <p>If you need replacement parts for septic tanks, call us today! Tane Drain Septic Services will either have or can source the part you need fast and offer septic tank part installation services to ensure your parts are fitted orrectly and work at optimum efficiency for longer. And often we can offer same day service when you’re in a bind.</p>
  <span class="btn">More Info</span>
</div>

<div class="abs enquiry"></div>
<p class="abs enq-label">Free Quote Form</p>
<p class="abs enq-title">Make An Enquiry</p>
<p class="abs enq-note">Fil out the form below and we will<br>contact you within <strong>4 Hrs</strong></p>
<div class="abs field" style="left:398px;top:810px">Name</div>
<div class="abs field" style="left:398px;top:843px">E-Mail ID</div>
<div class="abs field" style="left:398px;top:876px">Phone</div>
<div class="abs field details" style="left:588px;top:810px">Details</div>
<span class="abs btn send">SEND</span>

<div class="abs footer"></div>
<p class="abs foot-head" style="left:121px;top:971px">QUICK LINKS</p>
<ul class="abs links">
  <li>Home</li><li>About</li><li>Deciphering Your Septic tank</li><li>Servicing &amp; Maintenance</li><li>Parts</li><li>Free Quote</li><li>Contact</li>
</ul>
<p class="abs foot-head" style="left:277px;top:971px">COMPANY GUARANTEE TO YOU...</p>
<p class="abs guarantee">Tane Drain Septic Services travel throughout the Auckland region. Owner Rewi promises they will go through your system with a fine tooth comb and provide a comprehensive service. Tane Drain Septic Services aim to give clients more than they expect from their septic tank service.</p>

<div class="abs promo" style="top:966px">
  <svg width="17" height="17" viewBox="0 0 17 17"><circle cx="8.5" cy="8.5" r="8.5" fill="#fff"/><path d="M7 5l3.5 3.5L7 12" stroke="#0fa44f" stroke-width="2" fill="none"/></svg>
  <div><strong>Need your septic tank cleaned?</strong><br>Talk to the team at Kereru Tank Cleaning Services!</div>
</div>
<div class="abs promo" style="top:1039px">
  <svg width="17" height="17" viewBox="0 0 17 17"><circle cx="8.5" cy="8.5" r="8.5" fill="#fff"/><path d="M7 5l3.5 3.5L7 12" stroke="#0fa44f" stroke-width="2" fill="none"/></svg>
  <div><strong>For all polymer fabricated products</strong><br>Talk to the team at Ponga Plastics Limited!</div>
</div>

<p class="abs copy">© 2014Company Name ,All Rights Reserved</p>
<div class="abs social"><span style="background:#3b5998"></span><span style="background:#29a9e1"></span><span style="background:#0e76a8"></span></div>
</body>
</html>
```